Design a Professional Business Card for Velmora Arcs

Design a business card for Velmora Arcs, we are a National Sport Court Company.

West Region Address: 4175 Quill Harbor Ln, Suite #215 Ravelton, Norvale 80467
East Region Address: 3817 Tamsin Rd E, Pellham Bay, Sorento 34583

Target Market(s)

High End Residential & Institutional Clients

Industry/Entity Type

Design & Construction

Contact Information for Business Card

Logo/Brand/Colors/ name, number (provided in comments)

Requirements
Must have
• Colors only provided in logo
Should not have
• Any other colors not in existing logo (attached)

```html
<!DOCTYPE html>
<html lang="en">
<head>
<meta charset="utf-8">
<title>Velmora Arcs — Business Card</title>
<link href="https://fonts.googleapis.com/css2?family=Open+Sans:wght@400;600;700;800&display=swap" rel="stylesheet">
<style>
  :root {
    --navy: #1e3566;
    --green: #006b3a;
    --teal: #0f5252;
    --ink: #1f2a3a;
    --white: #ffffff;
    --mist: #e7e9ef;
    --mint: #e9f1ec;
    --backdrop: #c9c9c9;
  }
  * { box-sizing: border-box; margin: 0; padding: 0; }
  html, body { width: 1200px; height: 900px; overflow: hidden; }
  body {
    background: var(--backdrop);
    font-family: "Open Sans", Arial, sans-serif;
    position: relative;
  }
  .card {
    position: absolute;
    width: 620px;
    height: 354px;
    border-radius: 26px;
    overflow: hidden;
    box-shadow: 0 10px 24px rgba(0,0,0,0.25);
  }
  /* Front */
  .card-front {
    left: 70px; top: 70px;
    background: linear-gradient(160deg, var(--green) 0%, var(--teal) 45%, var(--navy) 100%);
  }
  .card-front .halo {
    position: absolute;
    width: 300px; height: 300px;
    right: 60px; top: -10px;
    border-radius: 50%;
    background: rgba(255,255,255,0.05);
  }
  .card-front .brand {
    position: absolute;
    inset: 0;
    display: flex; align-items: center; justify-content: center; gap: 20px;
  }
  .brand-dot {
    width: 70px; height: 70px; border-radius: 50%;
    background: var(--white);
  }
  .card-front .brand-name {
    color: var(--white);
    font-weight: 800;
    font-size: 52px;
    letter-spacing: 4px;
    text-transform: uppercase;
    line-height: 1;
  }
  /* Back */
  .card-back {
    left: 510px; top: 476px;
    background: var(--white);
  }
  .card-back .halo {
    position: absolute;
    width: 300px; height: 300px;
    left: 250px; top: -70px;
    border-radius: 50%;
    background: var(--mist);
  }
  .card-back .panel {
    position: absolute;
    right: 0; top: 0;
    width: 170px; height: 150px;
    background: var(--mint);
  }
  .card-back .brand {
    position: absolute; left: 34px; top: 44px;
    display: flex; align-items: center; gap: 14px;
  }
  .card-back .brand-dot { width: 56px; height: 56px; background: var(--green); }
  .card-back .brand-name {
    color: var(--navy); font-weight: 800; font-size: 30px;
    letter-spacing: 2px; text-transform: uppercase; line-height: 1;
  }
  .person { position: absolute; left: 34px; top: 132px; }
  .person-name { color: var(--navy); font-weight: 800; font-size: 19px; text-transform: uppercase; letter-spacing: .5px; }
  .person-name .credential { color: var(--green); font-weight: 600; font-size: 15px; text-transform: none; }
  .person-title { color: var(--ink); font-size: 14px; margin-top: 2px; }
  .contacts { position: absolute; left: 34px; top: 216px; list-style: none; }
  .contacts li {
    display: flex; align-items: center; gap: 8px;
    color: var(--ink); font-size: 13.5px; line-height: 1; margin-bottom: 7px;
  }
  .icon {
    width: 18px; height: 18px; border-radius: 50%;
    background: var(--navy); flex: none;
    display: flex; align-items: center; justify-content: center;
  }
  .icon svg { width: 11px; height: 11px; }
  .region { position: absolute; top: 212px; font-size: 13px; color: var(--ink); line-height: 1.4; }
  .region-west { left: 300px; }
  .region-east { left: 462px; top: 168px; }
  .region-title {
    display: flex; align-items: center; gap: 6px;
    font-weight: 700; font-size: 14px; text-transform: uppercase; margin-bottom: 2px;
  }
  .region-west .region-title { color: var(--navy); }
  .region-east .region-title { color: var(--green); }
  .region p { padding-left: 24px; }
</style>
</head>
<body>

<section class="card card-front">
  <div class="halo"></div>
  <div class="brand">
    <div class="brand-dot"></div>
    <div class="brand-name">Velmora<br>Arcs</div>
  </div>
</section>

<section class="card card-back">
  <div class="halo"></div>
  <div class="panel"></div>

  <div class="brand">
    <div class="brand-dot"></div>
    <div class="brand-name">Velmora<br>Arcs</div>
  </div>

  <div class="person">
    <div class="person-name">Dorian M. Halvers, <span class="credential">QLDA</span></div>
    <div class="person-title">CEO &amp; Founder</div>
  </div>

  <ul class="contacts">
    <li><span class="icon"><svg viewBox="0 0 24 24"><path fill="#fff" d="M6.6 10.8a15 15 0 0 0 6.6 6.6l2.2-2.2c.3-.3.7-.4 1-.2 1.1.4 2.3.6 3.6.6.6 0 1 .4 1 1V20c0 .6-.4 1-1 1A17 17 0 0 1 3 4c0-.6.4-1 1-1h3.5c.6 0 1 .4 1 1 0 1.3.2 2.5.6 3.6.1.3 0 .7-.2 1z"/></svg></span>(555) 555-0147 (Direct)</li>
    <li><span class="icon"><svg viewBox="0 0 24 24"><path fill="#fff" d="M6.6 10.8a15 15 0 0 0 6.6 6.6l2.2-2.2c.3-.3.7-.4 1-.2 1.1.4 2.3.6 3.6.6.6 0 1 .4 1 1V20c0 .6-.4 1-1 1A17 17 0 0 1 3 4c0-.6.4-1 1-1h3.5c.6 0 1 .4 1 1 0 1.3.2 2.5.6 3.6.1.3 0 .7-.2 1z"/></svg></span>1-800-555-0193</li>
    <li><span class="icon"><svg viewBox="0 0 24 24"><path fill="none" stroke="#fff" stroke-width="2.4" d="M3 6h18v12H3zM3 6l9 7 9-7"/></svg></span>dorian@velmoraarcs.com</li>
    <li><span class="icon"><svg viewBox="0 0 24 24"><g fill="none" stroke="#fff" stroke-width="2"><circle cx="12" cy="12" r="9"/><path d="M3 12h18M12 3c3 3 3 15 0 18M12 3c-3 3-3 15 0 18"/></g></svg></span>www.velmoraarcs.com</li>
  </ul>

  <div class="region region-west">
    <div class="region-title"><span class="icon"><svg viewBox="0 0 24 24"><path fill="#fff" d="M12 2a7 7 0 0 0-7 7c0 5 7 13 7 13s7-8 7-13a7 7 0 0 0-7-7zm0 9.5A2.5 2.5 0 1 1 12 6.5a2.5 2.5 0 0 1 0 5z"/></svg></span>West Region</div>
    <p>4175 Quill Harbor Ln,<br>Suite #215 Ravelton,<br>Norvale 80467</p>
  </div>

  <div class="region region-east">
    <div class="region-title"><span class="icon"><svg viewBox="0 0 24 24"><path fill="#fff" d="M12 2a7 7 0 0 0-7 7c0 5 7 13 7 13s7-8 7-13a7 7 0 0 0-7-7zm0 9.5A2.5 2.5 0 1 1 12 6.5a2.5 2.5 0 0 1 0 5z"/></svg></span>East Region</div>
    <p>3817 Tamsin Rd E,<br>Pellham Bay,<br>Sorento 34583</p>
  </div>
</section>

</body>
</html>
```